The Quiet Hour Safeguard Handbook

A book cover. The book will be marketed as a promotional item for financial advisors, financial planners, independent insurance agents, bankers, and any professional who views their role as guardian of their clients assets and helping them manage risk.

```html
<!DOCTYPE html>
<html lang="en">
<head>
<meta charset="utf-8">
<title>The Quiet Hour Safeguard Handbook</title>
<link href="https://fonts.googleapis.com/css2?family=Bebas+Neue&family=Bodoni+Moda:wght@700&family=Libre+Baskerville:wght@700&family=Montserrat:wght@700&family=Open+Sans:wght@700&display=swap" rel="stylesheet">
<style>
  :root {
    --navy: #0a1f3d;
    --orange: #f4993a;
    --white: #ffffff;
    --rocket-light: #dfe4ec;
    --rocket-dark: #16305a;
  }
  html, body {
    margin: 0;
    padding: 0;
    width: 849px;
    height: 1200px;
    overflow: hidden;
    background: var(--navy);
  }
  .cover {
    position: relative;
    width: 849px;
    height: 1200px;
    background: var(--navy);
    color: var(--white);
    overflow: hidden;
  }
  .motto {
    position: absolute;
    top: 52px;
    left: 0;
    width: 849px;
    margin: 0;
    text-align: center;
    font-family: "Open Sans", sans-serif;
    font-weight: 700;
    font-size: 15px;
    line-height: 24px;
    letter-spacing: 6.6px;
    color: var(--orange);
  }
  .rocket-art {
    position: absolute;
    left: 497px;
    top: 128px;
    width: 170px;
    height: 411px;
  }
  .title { margin: 0; font-weight: normal; }
  .title-kicker {
    position: absolute;
    left: 90px;
    top: 412px;
    font-family: "Bebas Neue", sans-serif;
    font-size: 86px;
    line-height: 0.82;
    letter-spacing: 8px;
  }
  .title-hero {
    position: absolute;
    left: 78px;
    top: 490px;
    font-family: "Bebas Neue", sans-serif;
    font-size: 205px;
    line-height: 0.82;
    letter-spacing: 0;
  }
  .title-unit {
    position: absolute;
    left: 440px;
    top: 569px;
    font-family: "Montserrat", sans-serif;
    font-weight: 700;
    font-size: 72px;
    line-height: 1;
    letter-spacing: 7px;
  }
  .title-main {
    position: absolute;
    left: 80px;
    top: 719px;
    font-family: "Bodoni Moda", serif;
    font-weight: 700;
    font-size: 80px;
    line-height: 88px;
    letter-spacing: 3px;
  }
  .tagline {
    position: absolute;
    left: 610px;
    top: 815px;
    margin: 0;
    font-family: "Open Sans", sans-serif;
    font-weight: 700;
    font-size: 14px;
    line-height: 21px;
    letter-spacing: 2px;
    color: var(--orange);
  }
  .rule {
    position: absolute;
    left: 87px;
    width: 679px;
    height: 1px;
    background: var(--white);
  }
  .rule-top { top: 990px; }
  .rule-bottom { top: 1080px; }
  .author {
    position: absolute;
    left: 0;
    top: 1010px;
    width: 849px;
    margin: 0;
    text-align: center;
    font-family: "Libre Baskerville", serif;
    font-weight: 700;
    font-size: 40px;
    line-height: 50px;
    letter-spacing: 5px;
    color: var(--orange);
  }
  .credentials {
    position: absolute;
    left: 0;
    top: 1129px;
    width: 849px;
    margin: 0;
    text-align: center;
    font-family: "Open Sans", sans-serif;
    font-weight: 700;
    font-size: 20px;
    line-height: 24px;
    letter-spacing: 2.5px;
  }
</style>
</head>
<body>
  <main class="cover">
    <p class="motto">IT'S BETTER TO HAVE IT AND NOT NEED IT<br>THAN NEED IT AND NOT HAVE IT.</p>

    <svg class="rocket-art" role="img" aria-label="Illustration of a retro rocket ship pointing upward" viewBox="0 0 170 411">
      <defs>
        <linearGradient id="rocketTone" x1="0" y1="0" x2="0" y2="1">
          <stop offset="0" stop-color="var(--rocket-light)" stop-opacity="0.9"/>
          <stop offset="1" stop-color="var(--rocket-dark)" stop-opacity="0.9"/>
        </linearGradient>
      </defs>
      <rect x="0" y="0" width="170" height="411" rx="8" fill="url(#rocketTone)"/>
    </svg>

    <h1 class="title">
      <span class="title-kicker">THE</span>
      <span class="title-hero">QUIET</span>
      <span class="title-unit">HOUR</span>
      <span class="title-main">SAFEGUARD<br>HANDBOOK</span>
    </h1>

    <p class="tagline">PROTECT YOURSELF<br>AND YOUR FAMILY<br>IN THE AI AGE</p>

    <div class="rule rule-top"></div>
    <p class="author">MARCUS T. HOLLOWELL</p>
    <div class="rule rule-bottom"></div>

    <p class="credentials">RISK ADVISOR | WEALTH PROTECTOR | FAMILY ADVOCATE</p>
  </main>
</body>
</html>
```